Simple Webpage for Company that offer IT Security Services

Company Type: Penetration Tests, IT Security Services, Security Audits
Company Name: VaultHaven
Navigation Style: similar to https://www.brivanta-example.com/en/ with Top Navigation (and submenu's)
Top Navigation Items: Services, About Us, Contact
Industry/Entity Type
It Company
Coding
Coded - Design and coding required

```html
<!DOCTYPE html>
<html lang="en">
<head>
<meta charset="utf-8">
<title>VaultHaven – IT Security Services</title>
<link rel="stylesheet" href="https://fonts.googleapis.com/css2?family=Open+Sans:ital,wght@0,400;0,600;0,700;1,400&family=Roboto:wght@400;500;700;900&display=swap">
<style>
:root{
  --blue:#1c7cc4;
  --blue-band:#2280c8;
  --blue-dark:#0f3d6e;
  --navy:#0a1e3c;
  --ink:#222a33;
  --text:#555c63;
  --muted:#8a9097;
  --line:#d9dde1;
  --pale:#d3e7f1;
  --white:#ffffff;
}
*{box-sizing:border-box;margin:0;padding:0}
html,body{width:1200px;height:2486px;overflow:hidden;background:var(--white)}
body{font-family:"Open Sans",Arial,sans-serif;color:var(--text);position:relative}
.abs{position:absolute}
a{color:inherit;text-decoration:none}
ul{list-style:none}

/* header */
.site-header{position:absolute;top:0;left:0;width:1200px;height:83px;background:var(--white);border-top:4px solid var(--blue);z-index:3}
.brand{position:absolute;left:99px;top:0;height:79px;display:flex;align-items:center;gap:10px;font-family:"Roboto",sans-serif;font-weight:700;font-size:25px;color:var(--ink);letter-spacing:.3px}
.brand-mark{width:32px;height:32px;background:var(--blue)}
.main-nav{position:absolute;top:0;right:143px;height:79px;display:flex;align-items:center;gap:46px;font-family:"Roboto",sans-serif;font-weight:500;font-size:16px;color:var(--ink);white-space:nowrap}
.main-nav .active{color:var(--blue)}
.search-icon{position:absolute;right:97px;top:30px}

/* hero */
.hero{position:absolute;top:83px;left:0;width:1200px;height:500px;overflow:hidden;
  background:radial-gradient(ellipse at 50% 30%,#2f6fb8 0%,#173f78 35%,#0b2148 70%,#061531 100%)}
.hero-title{position:absolute;top:110px;width:100%;text-align:center;font-family:"Roboto",sans-serif;font-weight:700;font-size:80px;color:var(--white);letter-spacing:1px}
.hero-sub{position:absolute;top:200px;width:100%;text-align:center;font-family:"Roboto",sans-serif;font-size:25px;line-height:36px;color:var(--white)}
.btn-hero{position:absolute;left:500px;top:318px;width:198px;height:38px;border:2px solid var(--white);border-radius:20px;background:var(--blue);color:var(--white);font-size:13px;font-weight:700;display:flex;align-items:center;justify-content:center;letter-spacing:.3px}
.dots{position:absolute;top:403px;width:100%;display:flex;justify-content:center;gap:5px}
.dots span{width:14px;height:14px;border:2px solid var(--white);border-radius:50%}
.dots span.on{background:var(--white)}
.hero-cut{position:absolute;left:0;bottom:0}

/* welcome */
.welcome-title{left:99px;top:630px;font-family:"Roboto",sans-serif;font-weight:500;font-size:32px;color:var(--ink)}
.welcome-text{left:99px;top:690px;width:462px;font-size:12px;line-height:25px;color:var(--text)}
.welcome-text p+p{margin-top:25px}
.btn-outline{border:1px solid #9aa3ab;border-radius:20px;color:var(--blue);font-size:12.5px;font-weight:700;display:flex;align-items:center;justify-content:center;background:var(--white)}
.btn-read{left:99px;top:886px;width:130px;height:35px}
.video-frame{left:606px;top:641px;width:495px;height:287px;border:1px solid var(--line);padding:3px;background:var(--white)}
.video-art{width:100%;height:100%;background:linear-gradient(135deg,#7fb4d6 0%,#3a7fb3 45%,#1c3f63 100%);position:relative}
.play{position:absolute;left:216px;top:108px}

/* services */
.services{position:absolute;top:994px;left:0;width:1200px;height:577px;background:var(--blue-band)}
.section-title{position:absolute;width:100%;text-align:center;font-family:"Roboto",sans-serif;font-weight:500;font-size:30px}
.services .section-title{top:48px;color:var(--white)}
.card{position:absolute;top:118px;width:317px;height:414px;background:var(--white);border:3px solid var(--white);text-align:center;overflow:hidden}
.card-art{position:absolute;left:0;top:0;width:311px;height:205px;clip-path:polygon(0 0,100% 0,100% 165px,50% 205px,0 165px)}
.art-pen{background:linear-gradient(135deg,#0b2c70 0%,#1656b0 55%,#0a1f55 100%)}
.art-it{background:linear-gradient(135deg,#c9ccd2 0%,#6e7684 50%,#2d3546 100%)}
.art-audit{background:linear-gradient(135deg,#e6c79d 0%,#8c7b6c 45%,#3f4e66 100%)}
.card-icon{position:absolute;left:119px;top:164px;width:74px;height:74px;border-radius:50%;background:var(--blue);border:4px solid var(--white);display:flex;align-items:center;justify-content:center}
.card h3{position:absolute;left:0;top:256px;width:100%;font-family:"Roboto",sans-serif;font-weight:500;font-size:21px;color:var(--ink)}
.card p{position:absolute;top:294px;left:24px;width:263px;font-size:12.5px;line-height:22px;color:var(--text)}
.card .more{position:absolute;display:block;left:0;top:372px;width:100%;text-align:center;font-size:12.5px;font-weight:700;color:var(--blue)}

/* blog */
.blog .section-title{top:1625px;color:var(--ink)}
.post{position:absolute;top:1707px;width:330px;height:94px}
.post-thumb{position:absolute;left:0;top:0;width:98px;height:93px;border:1px solid var(--line);padding:3px;background:var(--white)}
.post-thumb div{width:100%;height:100%}
.th1{background:linear-gradient(135deg,#9ec7e4,#2a6ea8 60%,#16365c)}
.th2{background:linear-gradient(180deg,#cfe3f4,#5d8fc0 55%,#1d3552)}
.th3{background:linear-gradient(135deg,#3fb8c8,#156a8e 55%,#0b2d49)}
.post h4{position:absolute;left:121px;top:-4px;width:210px;font-weight:600;font-size:14px;line-height:21px;color:var(--ink)}
.post-date{position:absolute;left:121px;top:48px;display:flex;align-items:center;gap:8px;font-size:12px;color:var(--muted)}
.btn-blog{left:500px;top:1849px;width:198px;height:40px}

/* testimonial */
.testimonial{position:absolute;top:1897px;left:0;width:1200px;height:257px;background:var(--pale)}
.avatar{position:absolute;left:107px;top:88px;width:130px;height:130px;border-radius:50%;border:4px solid var(--white);background:radial-gradient(circle at 50% 40%,#c9ab96 0%,#8f7a70 45%,#3d5f85 100%);box-shadow:0 0 0 1px #bcd2dd}
.quote-rule{position:absolute;left:270px;top:88px;width:1px;height:123px;background:#9fb3bd}
.quote{position:absolute;left:303px;top:93px;width:780px;font-style:italic;font-size:14px;line-height:26px;color:#6c747b}
.quote-name{position:absolute;left:306px;top:186px;font-family:"Roboto",sans-serif;font-weight:500;font-size:18px;color:var(--blue)}
.arrow{position:absolute;top:138px}

/* footer */
.footer-brand{left:99px;top:2268px;display:flex;align-items:center;gap:10px;font-family:"Roboto",sans-serif;font-weight:700;font-size:30px;color:var(--ink)}
.footer-brand .brand-mark{width:36px;height:36px}
.foot-col{top:2208px}
.foot-col h5{font-family:"Roboto",sans-serif;font-weight:500;font-size:18px;color:var(--ink);margin-bottom:14px}
.foot-links li{font-size:12px;line-height:28px;color:var(--text)}
.foot-news p{width:260px;font-size:12px;line-height:22px;color:var(--text)}
.email-field{margin-top:16px;width:253px;border-bottom:1px solid var(--line);padding:0 0 8px 10px;font-size:11px;color:var(--muted)}
.btn-sub{margin-top:16px;width:96px;height:31px;font-size:11px}
.contact-list li{position:relative;padding-left:30px;font-size:12px;line-height:22px;color:var(--text)}
.contact-list svg{position:absolute;left:0;top:4px}
.foot-rule{left:99px;top:2413px;width:1002px;height:1px;background:var(--line)}
.copyright{left:99px;top:2439px;font-size:12px;color:var(--text)}
.social{left:976px;top:2436px;display:flex;gap:7px}
.social span{width:26px;height:26px;border-radius:50%;border:1px solid #9bb9d4;background:var(--white)}
</style>
</head>
<body>

<header class="site-header">
  <div class="brand"><span class="brand-mark"></span>VAULTHAVEN</div>
  <nav>
    <ul class="main-nav">
      <li class="active">HOME</li>
      <li>ABOUT US</li>
      <li>SERVICES</li>
      <li>BLOG</li>
      <li>CONTACT US</li>
    </ul>
  </nav>
  <svg class="search-icon" width="18" height="18" viewBox="0 0 18 18"><circle cx="7.5" cy="7.5" r="5.5" fill="none" stroke="#222a33" stroke-width="2.4"/><line x1="11.5" y1="11.5" x2="16" y2="16" stroke="#222a33" stroke-width="2.8" stroke-linecap="round"/></svg>
</header>

<section class="hero" role="img" aria-label="Photo of a dimly lit server room aisle with racks of blinking equipment">
  <h1 class="hero-title">VAULTHAVEN</h1>
  <p class="hero-sub">We provide IT security services, include Penetration Tests,<br>IT Security Services, Security Audits.</p>
  <a class="btn-hero">GET MORE INFO &gt;&gt;</a>
  <div class="dots"><span class="on"></span><span></span><span></span><span></span></div>
  <svg class="hero-cut" width="1200" height="500" viewBox="0 0 1200 500"><polygon points="0,409 600,500 1200,409 1200,500 0,500" fill="#ffffff"/></svg>
</section>

<section class="welcome">
  <h2 class="abs welcome-title">Welcome to VaultHaven</h2>
  <div class="abs welcome-text">
    <p>At vero eos et accusamus et iusto odio dignissimos ducimus qui blanditiis praesent ium voluptatum deleniti atque corrupti quo.</p>
    <p>Dolores et quas molestias excepturi sint occaecati cupiditate non provident similiq ue sunt in culpa qui officia deserunt mollitia animi, id est laborum et dolorum fug t harum quidem rerum facilis est et expedita voluptas assumenda est, omnis dolorr epellend poribus autem quibusdam et aut officiis.</p>
  </div>
  <a class="abs btn-outline btn-read">READ MORE &gt;&gt;</a>
  <div class="abs video-frame">
    <div class="video-art" role="img" aria-label="Photo of a businessman touching a glowing network of security icons">
      <svg class="play" width="62" height="62" viewBox="0 0 62 62"><circle cx="31" cy="31" r="30" fill="#2b3440" fill-opacity=".75"/><polygon points="24,18 45,31 24,44" fill="#ffffff"/></svg>
    </div>
  </div>
</section>

<section class="services">
  <h2 class="section-title">Our Services</h2>

  <article class="card" style="left:99px">
    <div class="card-art art-pen" role="img" aria-label="Illustration of a shield with a check mark on a blue digital background"></div>
    <div class="card-icon"><svg width="34" height="34" viewBox="0 0 34 34"><path d="M17 3 L29 8 V16 C29 24 23 29 17 31 C11 29 5 24 5 16 V8 Z" fill="#fff"/><polyline points="11,17 15,21 23,12" fill="none" stroke="#1c7cc4" stroke-width="3"/></svg></div>
    <h3>Penetration Tests</h3>
    <p>Nam libero tempore, cum soluta nobis est el igendi optio cumque nihil impedit quo minus id quod maxime placeat facere pos</p>
    <a class="more">READ MORE &gt;&gt;</a>
  </article>

  <article class="card" style="left:442px">
    <div class="card-art art-it" role="img" aria-label="Photo of a hand touching hexagon security keywords in front of server racks"></div>
    <div class="card-icon"><svg width="34" height="34" viewBox="0 0 34 34"><circle cx="13" cy="19" r="8" fill="none" stroke="#fff" stroke-width="5" stroke-dasharray="4 2.3"/><circle cx="13" cy="19" r="3" fill="#fff"/><circle cx="25" cy="9" r="5" fill="none" stroke="#fff" stroke-width="3.5" stroke-dasharray="3 1.8"/></svg></div>
    <h3>IT Security Services</h3>
    <p>Nam libero tempore, cum soluta nobis est el igendi optio cumque nihil impedit quo minus id quod maxime placeat facere pos</p>
    <a class="more">READ MORE &gt;&gt;</a>
  </article>

  <article class="card" style="left:784px">
    <div class="card-art art-audit" role="img" aria-label="Photo of hands holding a smartphone in front of a laptop"></div>
    <div class="card-icon"><svg width="30" height="34" viewBox="0 0 30 34"><rect x="3" y="2" width="24" height="30" rx="2" fill="#fff"/><rect x="7" y="6" width="16" height="6" fill="#1c7cc4"/><g fill="#1c7cc4"><rect x="7" y="15" width="4" height="3"/><rect x="13" y="15" width="4" height="3"/><rect x="19" y="15" width="4" height="3"/><rect x="7" y="21" width="4" height="3"/><rect x="13" y="21" width="4" height="3"/><rect x="19" y="21" width="4" height="3"/><rect x="7" y="26" width="4" height="3"/><rect x="13" y="26" width="4" height="3"/><rect x="19" y="26" width="4" height="3"/></g></svg></div>
    <h3>Security Audits</h3>
    <p>Nam libero tempore, cum soluta nobis est el igendi optio cumque nihil impedit quo minus id quod maxime placeat facere pos</p>
    <a class="more">READ MORE &gt;&gt;</a>
  </article>
</section>

<section class="blog">
  <h2 class="section-title">Latest Blog</h2>

  <article class="post" style="left:99px">
    <div class="post-thumb"><div class="th1" role="img" aria-label="Photo of a person using cloud and gear icons on a screen"></div></div>
    <h4>At vero eos et accusamus et iusto odio dignissimos</h4>
    <div class="post-date"><svg width="11" height="11" viewBox="0 0 11 11"><rect x="0" y="1" width="11" height="10" fill="#1c7cc4"/><rect x="1.5" y="4" width="8" height="5.5" fill="#fff"/></svg>25/02/2016</div>
  </article>

  <article class="post" style="left:444px">
    <div class="post-thumb"><div class="th2" role="img" aria-label="Photo of a bright server room corridor"></div></div>
    <h4>At vero eos et accusamus et iusto odio dignissimos</h4>
    <div class="post-date"><svg width="11" height="11" viewBox="0 0 11 11"><rect x="0" y="1" width="11" height="10" fill="#1c7cc4"/><rect x="1.5" y="4" width="8" height="5.5" fill="#fff"/></svg>25/02/2016</div>
  </article>

  <article class="post" style="left:795px">
    <div class="post-thumb"><div class="th3" role="img" aria-label="Illustration of a padlock on a teal digital background"></div></div>
    <h4>At vero eos et accusamus et iusto odio dignissimos</h4>
    <div class="post-date"><svg width="11" height="11" viewBox="0 0 11 11"><rect x="0" y="1" width="11" height="10" fill="#1c7cc4"/><rect x="1.5" y="4" width="8" height="5.5" fill="#fff"/></svg>25/02/2016</div>
  </article>

  <a class="abs btn-outline btn-blog">VIEW MORE BLOG &gt;&gt;</a>
</section>

<section class="testimonial">
  <svg class="arrow" style="left:36px" width="18" height="30" viewBox="0 0 18 30"><polyline points="15,2 3,15 15,28" fill="none" stroke="#ffffff" stroke-width="2.5"/></svg>
  <div class="avatar" role="img" aria-label="Portrait photo of the client giving the testimonial"></div>
  <div class="quote-rule"></div>
  <p class="quote">Nam libero tempore, cum soluta nobis est eligendi optio cumque nihil impedit quo minus id quod maxime placeat facere possimus, omnis voluptas assumenda est, omnis dolor repellendus. Temporibus autem quibusdam et aut officiis debitis aut rerum necessitatibus saepe eveniet ut et voluptates repudiandae sint et molestiae</p>
  <p class="quote-name">- Marco Ferrandi</p>
  <svg class="arrow" style="left:1146px" width="18" height="30" viewBox="0 0 18 30"><polyline points="3,2 15,15 3,28" fill="none" stroke="#ffffff" stroke-width="2.5"/></svg>
</section>

<footer class="site-footer">
  <div class="abs footer-brand"><span class="brand-mark"></span>VAULTHAVEN</div>

  <div class="abs foot-col" style="left:432px">
    <h5>Information</h5>
    <ul class="foot-links"><li>Home</li><li>About Us</li><li>Services</li><li>Blog</li><li>Contact Us</li></ul>
  </div>

  <div class="abs foot-col foot-news" style="left:620px">
    <h5>Newsletter Subscription</h5>
    <p>Register your Email Address to get information about us</p>
    <div class="email-field">Email Address</div>
    <a class="btn-outline btn-sub">SUBSCRIBE</a>
  </div>

  <div class="abs foot-col" style="left:913px">
    <h5>Contact Us</h5>
    <ul class="contact-list">
      <li><svg width="11" height="15" viewBox="0 0 11 15"><path d="M5.5 0 C8.5 0 11 2.4 11 5.4 C11 9 5.5 15 5.5 15 C5.5 15 0 9 0 5.4 C0 2.4 2.5 0 5.5 0 Z" fill="#1c7cc4"/><circle cx="5.5" cy="5.3" r="2" fill="#fff"/></svg>Via dei Tigli, 27<br>10121 Torino - Italy</li>
      <li style="margin-top:17px"><svg width="14" height="14" viewBox="0 0 14 14"><path d="M3 0 L5.5 3.5 L4 5.5 C5 7.5 6.5 9 8.5 10 L10.5 8.5 L14 11 L12 14 C6 13.5 0.5 8 0 2 Z" fill="#1c7cc4"/></svg>+1-555-014-2290</li>
      <li style="margin-top:20px"><svg width="15" height="11" viewBox="0 0 15 11"><rect width="15" height="11" fill="#1c7cc4"/><polyline points="0.5,0.5 7.5,6 14.5,0.5" fill="none" stroke="#fff" stroke-width="1.4"/></svg>info@vaulthaven.com</li>
    </ul>
  </div>

  <div class="abs foot-rule"></div>
  <p class="abs copyright">Copyrights © 2017, VaultHaven.. All rights reserved.</p>
  <div class="abs social"><span></span><span></span><span></span><span></span></div>
</footer>

</body>
</html>
```